Bright Orchard
Bright & Fun-filled
Talia Brennick
Certified Holistic Wellness Coach, NLP Practitioner
no address pls
talia@brightorchard.com
www.brightorchard.com
To love oneself is the beginning of a lifelong romance. --Edwin Tarrow

```html
<!DOCTYPE html>
<html lang="en">
<head>
<meta charset="utf-8">
<title>Bright Orchard – Business Card</title>
<link rel="stylesheet" href="https://fonts.googleapis.com/css2?family=Open+Sans:wght@400;600;700&display=swap">
<style>
  :root {
    --bg: #e9e6e2;
    --card: #ffffff;
    --rose: #e5185a;
    --rule: #b9b9b9;
    --ink: #4a4a4a;
    --ink-soft: #5b5b5b;
    --ink-muted: #7a7a7a;
  }
  * { margin: 0; padding: 0; box-sizing: border-box; }
  html, body {
    width: 1200px; height: 780px; overflow: hidden;
    background: var(--bg);
    font-family: "Open Sans", Arial, sans-serif;
  }
  .card {
    position: absolute; left: 110px; top: 100px;
    width: 980px; height: 580px;
    background: var(--card);
    border-radius: 34px;
    box-shadow: 0 10px 30px rgba(0,0,0,.18);
    overflow: hidden;
  }
  .card__rule {
    position: absolute; left: 0; right: 0; height: 3px;
    background: var(--rule);
  }
  .card__rule--top { top: 52px; }
  .card__rule--bottom { top: 214px; }
  .card__band {
    position: absolute; left: 0; right: 0; top: 62px; height: 144px;
    background: var(--rose);
    color: #fff; text-align: center;
    padding-top: 22px;
  }
  .card__name { font-size: 36px; font-weight: 700; letter-spacing: .3px; }
  .card__title { font-size: 25px; font-weight: 400; line-height: 1.3; margin-top: 4px; }
  .brand {
    position: absolute; left: 0; right: 0; top: 268px;
    display: flex; justify-content: center; align-items: center; gap: 22px;
  }
  .brand__name {
    font-size: 82px; font-weight: 600; color: var(--ink);
    letter-spacing: -1px; line-height: 1.1;
  }
  .brand__dot {
    width: 44px; height: 44px; border-radius: 50%;
    background: var(--rose);
  }
  .quote {
    position: absolute; left: 80px; right: 80px; top: 400px;
    text-align: center; font-size: 19px; color: var(--ink-muted);
    line-height: 1.4;
  }
  .quote__author { color: var(--rose); font-weight: 600; }
  .contacts {
    position: absolute; left: 60px; right: 60px; bottom: 44px;
    display: flex; justify-content: space-between; align-items: center;
    font-size: 22px; color: var(--ink-soft);
  }
  .contact { display: flex; align-items: center; gap: 10px; }
  .contact svg { width: 26px; height: 26px; flex: none; }
</style>
</head>
<body>
  <div class="card">
    <div class="card__rule card__rule--top"></div>
    <div class="card__band">
      <div class="card__name">Talia Brennick</div>
      <div class="card__title">Certified Holistic Wellness Coach,<br>NLP Practitioner</div>
    </div>
    <div class="card__rule card__rule--bottom"></div>

    <div class="brand">
      <span class="brand__name">Bright Orchard</span>
      <span class="brand__dot"></span>
    </div>

    <p class="quote">“To love oneself is the beginning of a lifelong romance.” <span class="quote__author">— Edwin Tarrow</span></p>

    <div class="contacts">
      <div class="contact">
        <svg viewBox="0 0 24 24" aria-hidden="true"><rect x="6" y="2" width="12" height="20" rx="2.5" fill="var(--rose)"/><rect x="8.5" y="5" width="7" height="10" fill="#fff"/><circle cx="12" cy="18.5" r="1.3" fill="#fff"/></svg>
        <span>555.014.2286</span>
      </div>
      <div class="contact">
        <svg viewBox="0 0 24 24" aria-hidden="true"><rect x="2" y="5" width="20" height="14" rx="2" fill="var(--rose)"/><path d="M3 6.5 L12 13 L21 6.5" fill="none" stroke="#fff" stroke-width="1.8"/></svg>
        <span>talia@brightorchard.com</span>
      </div>
      <div class="contact">
        <svg viewBox="0 0 24 24" aria-hidden="true"><circle cx="12" cy="12" r="10" fill="var(--rose)"/><circle cx="12" cy="12" r="6.5" fill="none" stroke="#fff" stroke-width="1.6"/><path d="M5.5 12 H18.5 M12 5.5 V18.5" stroke="#fff" stroke-width="1.4"/></svg>
        <span>www.brightorchard.com</span>
      </div>
    </div>
  </div>
</body>
</html>
```